Business Cards for an 'affordable luxury' inner city home builder in Calgary.

We need a business card design that emulates the progressive, innovative, culture of our company and the modern style of our homes. Use our website www.velmarcrest-ab.com as a reference for the product we build.

Our company builds homes in the inner city space of Calgary, Alberta. We build affordable luxury.

Target Market(s)

Young professional Families

Contact Information for Business Card

Try to maintain consistency with the logo font and the card font.

Requirements
Must have
• The details must include: Name, education, title, phone number, website and email (Address is not as important)
• The design must be uniques (like our logo), elegant, sophisticated and modern.

```html
<!DOCTYPE html>
<html lang="en">
<head>
<meta charset="utf-8">
<title>Velmarcrest Homes Ltd — Business Cards</title>
<link href="https://fonts.googleapis.com/css2?family=Montserrat:wght@500;600&family=Roboto:wght@400;700&display=swap" rel="stylesheet">
<style>
  :root {
    --stage: #2b2b2b;
    --card-dark: #1f1f1f;
    --card-light: #ffffff;
    --ink: #2a2a2a;
    --ink-soft: #8a8a8a;
    --ink-faint: #a3a3a3;
    --white: #ffffff;
  }
  * { margin: 0; padding: 0; box-sizing: border-box; }
  html, body { width: 1200px; height: 900px; overflow: hidden; }
  body {
    background: var(--stage);
    position: relative;
    font-family: "Roboto", Arial, sans-serif;
  }
  .card {
    position: absolute;
    width: 560px;
    height: 320px;
    border-radius: 4px;
    box-shadow: 0 18px 40px rgba(0,0,0,.45);
    overflow: hidden;
  }
  .card--front { left: 30px; top: 190px; background: var(--card-dark); }
  .card--back  { left: 610px; top: 390px; background: var(--card-light); }

  .brand {
    position: absolute;
    display: flex;
    font-family: "Montserrat", Arial, sans-serif;
    font-weight: 500;
    text-transform: uppercase;
    letter-spacing: .06em;
    line-height: 1.05;
  }
  .brand__square { flex: none; }

  .card--front .brand {
    left: 60px; top: 90px;
    align-items: flex-start;
    gap: 34px;
    color: var(--white);
    font-size: 24px;
  }
  .card--front .brand__square {
    width: 200px; height: 200px;
    border: 14px solid var(--white);
    border-radius: 2px;
  }
  .card--front .brand__name { margin-top: 10px; }

  .card--back .brand {
    left: 40px; top: 48px;
    align-items: center;
    gap: 16px;
    color: var(--ink);
    font-size: 20px;
  }
  .card--back .brand__square { width: 30px; height: 30px; background: var(--ink); }

  .person { position: absolute; left: 40px; top: 168px; }
  .person__name { font-weight: 700; font-size: 24px; color: var(--ink); }
  .person__title { font-weight: 700; font-size: 14px; color: var(--ink-soft); margin-top: 6px; }
  .person__education { font-weight: 400; font-size: 13px; color: var(--ink-soft); margin-top: 4px; }
  .website { position: absolute; left: 40px; bottom: 30px; font-size: 14px; color: var(--ink-faint); }

  .contact { position: absolute; left: 330px; top: 60px; font-size: 14px; color: var(--ink-faint); }
  .contact__address { margin-bottom: 26px; }
  .contact__list { list-style: none; }
  .contact__item { display: flex; align-items: center; gap: 10px; margin-bottom: 6px; }
  .contact__item svg { width: 12px; height: 12px; fill: var(--ink); flex: none; }
</style>
</head>
<body>
  <section class="card card--front" aria-label="Card front">
    <div class="brand">
      <span class="brand__square"></span>
      <span class="brand__name">Velmarcrest<br>Homes Ltd</span>
    </div>
  </section>

  <section class="card card--back" aria-label="Card back">
    <div class="brand">
      <span class="brand__square"></span>
      <span class="brand__name">Velmarcrest<br>Homes Ltd</span>
    </div>

    <div class="person">
      <p class="person__name">Elias Moreau</p>
      <p class="person__title">Director</p>
      <p class="person__education">B.Sc. Civil Engineering</p>
    </div>
    <p class="website">www.velmarcrest-ab.com</p>

    <div class="contact">
      <p class="contact__address">248 17 Ave NE Calgary, AB</p>
      <ul class="contact__list">
        <li class="contact__item">
          <svg viewBox="0 0 24 24" aria-hidden="true"><path d="M6.6 10.8a15 15 0 0 0 6.6 6.6l2.2-2.2c.3-.3.7-.4 1-.2 1.1.4 2.3.6 3.6.6.6 0 1 .4 1 1V20c0 .6-.4 1-1 1A17 17 0 0 1 3 4c0-.6.4-1 1-1h3.5c.6 0 1 .4 1 1 0 1.3.2 2.5.6 3.6.1.3 0 .7-.2 1z"/></svg>
          <span>403-555-0148</span>
        </li>
        <li class="contact__item">
          <svg viewBox="0 0 24 24" aria-hidden="true"><path d="M7 1h10a2 2 0 0 1 2 2v18a2 2 0 0 1-2 2H7a2 2 0 0 1-2-2V3a2 2 0 0 1 2-2zm0 3v14h10V4zm5 15.2a1 1 0 1 0 0 2 1 1 0 0 0 0-2z"/></svg>
          <span>8500 310 762</span>
        </li>
        <li class="contact__item">
          <svg viewBox="0 0 24 24" aria-hidden="true"><path d="M2 5h20v14H2zm2 2v.5l8 5 8-5V7zm0 2.8V17h16V9.8l-8 5z"/></svg>
          <span>projects@velmarcrest-ab.com</span>
        </li>
      </ul>
    </div>
  </section>
</body>
</html>
```